Brochure design - brisk floors

i need a brochure design for my flooring business which is in the same style/theme as the attached file. the images chosen from clearvault should be focused on quality flooring and presented in a corporate and professional way. this design will be intended for printed brochures which i can hand to my clients as part of the sales process... I have a logo which should be included into the design (attached)
- This design should be ready for "Z" folded leaflet format - similar to the file attached
The design should present the images i attached in the brief
the design should follow the theme of the attached complete, sample brochure
the design needs to present the attached company logo in a clear and impressive way.
the design should allow for text boxes near each of the images

```html
<!DOCTYPE html>
<html lang="en">
<head>
<meta charset="utf-8">
<title>Brisk Floors – Z-fold Brochure</title>
<link rel="stylesheet" href="https://fonts.googleapis.com/css2?family=Montserrat:wght@300;400;500&display=swap">
<style>
  :root {
    --stage: #5b6164;
    --sky-photo-a: #63b6cf;
    --sky-photo-b: #3f8fab;
    --slate-overlay: rgba(70, 70, 72, 0.82);
    --teal-box: rgba(10, 40, 48, 0.94);
    --umber-box: rgba(33, 22, 15, 0.92);
    --accent: #46bfe2;
    --paper: #ffffff;
    --body-text: #e8eef0;
  }
  * { box-sizing: border-box; margin: 0; padding: 0; }
  html, body {
    width: 1200px; height: 900px; overflow: hidden;
    background: var(--stage);
    font-family: "Montserrat", sans-serif;
  }
  .brochure {
    position: absolute; left: 60px; top: 70px;
    width: 1080px; height: 760px;
    background: var(--paper);
    overflow: hidden;
    box-shadow: 0 18px 40px rgba(0,0,0,0.35);
  }
  .photo-sky {
    position: absolute; left: 0; top: 0; width: 360px; height: 760px;
    background: linear-gradient(160deg, var(--sky-photo-a), var(--sky-photo-b));
  }
  .artwork { position: absolute; left: 0; top: 0; }
  .text-panel {
    position: absolute;
    color: var(--body-text);
    font-weight: 300;
  }
  .story-panel {
    left: 70px; top: 190px; width: 290px; height: 570px;
    background: var(--teal-box);
    padding: 30px 26px 20px 34px;
    font-size: 10px; line-height: 1.38;
  }
  .story-panel h2 {
    font-weight: 300; font-size: 22px; color: var(--accent);
    margin-bottom: 10px; letter-spacing: 0.5px; line-height: 1.2;
  }
  .story-panel p { margin-bottom: 9px; }
  .feature-panel {
    left: 385px; top: 215px; width: 300px; height: 360px;
    background: var(--umber-box);
    padding: 50px 30px 20px 40px;
    font-size: 9px; line-height: 1.4;
  }
  .feature-panel p { margin-bottom: 8px; }
  .brand-mark {
    position: absolute; left: 810px; top: 300px;
    display: flex; align-items: center; gap: 12px;
    color: var(--accent);
    font-size: 30px; font-weight: 400; letter-spacing: 1px;
  }
  .brand-mark .brand-square {
    width: 34px; height: 34px; background: var(--accent);
  }
  .contact {
    position: absolute; left: 745px; top: 690px;
    color: var(--accent); font-size: 13px; font-weight: 500; line-height: 1.4;
    font-style: normal;
  }
</style>
</head>
<body>
<main class="brochure">
  <div class="photo-sky" role="img" aria-label="Photograph of a bright interior with blue-toned flooring"></div>

  <svg class="artwork" width="1080" height="760" viewBox="0 0 1080 760">
    <defs>
      <linearGradient id="wood" x1="0" y1="0" x2="1" y2="1">
        <stop offset="0" stop-color="#c8a385"/>
        <stop offset="1" stop-color="#a27b58"/>
      </linearGradient>
    </defs>
    <rect role="img" aria-label="Photograph of a smiling couple lying on a light oak wooden floor" x="360" y="0" width="720" height="760" fill="url(#wood)"/>
    <polygon class="slate-overlay" points="360,0 820,0 560,140 360,165" fill="rgba(55,45,40,0.55)"/>
    <polygon class="slate-overlay" points="880,0 1080,0 1080,760 700,760 820,260" fill="var(--slate-overlay)"/>
    <g class="fold-lines" fill="none" stroke="var(--paper)" stroke-width="9" stroke-linejoin="miter">
      <polyline points="360,168 560,142 825,0"/>
      <polyline points="600,0 1080,300"/>
      <polyline points="885,0 820,260 700,760"/>
    </g>
  </svg>

  <section class="text-panel story-panel">
    <h2>Ceariosam volum</h2>
    <p>As niam nimaximostia venihitat. Harchictis intiore hentotate venet estem harunt dignis nobit aute li bus nonsequis si voluptatia cuptae et aut essum nihic tem.</p>
    <p>Odita vent. Picia dias voluptam et et labo. Officid quostio eventis est volore aut aligendam, il idem utatur simporepro optaspi distion sequossitas expe consed magnam et volupti onsene velloris sitectore velic to quaspero tenis moloria vel illatio nsequia voloreped que dolorecum ad molupta sperio tessinvel essequa spernatur sequis acerene quaesto consequam litiistiam, sed quiderundi deniam quamet quodia corporit re, consendaerum fuga.</p>
    <p>Ut que nis di as ut eate exceferiam que re labores atur?</p>
    <p>Qui cuscia pra quis voluptae. Nemporae vendae vit ipient dellorerit corestrum lam que a consent.</p>
    <p>Um iusam, volut eic tet quid etur, cusdant.</p>
    <p>Eri iment experio optat optat. Natem sanimaximin endit, voluptatur?</p>
    <p>Ga. Otatquia qui dunt. Unti accus rectibus es cum enis et ilitin essit, asped molum ut hitatur sectorpos escipsam</p>
  </section>

  <section class="text-panel feature-panel">
    <p>As niam nimaximostia venihitat. Harchictis intiore hentotate venet estem harunt dignis nobit aute li</p>
    <p>bus nonsequis si voluptatia cuptae et aut essum nihic tem. Odita vent. Picia dias voluptam et et labo. Of</p>
    <p>ficid quostio eventis est volore aut aligendam, il idem utatur simporepro optaspi distion sequossitas</p>
    <p>expe consed magnam et volupti onsene velloris sitectore velic to quaspero tenis moloria vel illatio</p>
    <p>nsequia voloreped que dolorecum ad molupta sperio tessinvel essequa spernatur sequis acerene</p>
    <p>quaesto consequam litiistiam, sed quiderundi deniam quamet quodia corporit re, consendaerum</p>
  </section>

  <div class="brand-mark">
    <span class="brand-square"></span>
    <span class="brand-name">brisk floors</span>
  </div>

  <address class="contact">
    www.briskfloors.com<br>
    info@briskfloors.com
  </address>
</main>
</body>
</html>
```